Software company WebSite Design (enterprise level SW, Mobile apps, HW prototypes)

We need design for our new webpages. We got new logo and new business cards and we need webdesign which will be match with those two.
We are dealing with corporate level software development - enterprise level portals, development of optimalization SW, route planning optimalizations. For a few months we are developing mobile applications for companies.
IMPORTANT is to express the cutting edge technological company.

Target Market(s)

IT company customers

Industry/Entity Type

Business

Number of Pages Required

2 page

Requirements
Must have
• Project needs to have landing page and product detail page. Design needs to be created including full font and example images as there would be a real webpage. Design should be clean, modern and expressing hi-tech level of the company.
• Example of well designer web pages - www.quorvelt.com, www.brandissa.com - We like the font formatting and font designs (colors, placing, etc - its professional).
• Attached image contains screenshot from old web landing page. It contains basic sections of our business (Simulation Tools, Enterprise Intranet Systems, Hi-tech web presentations, Supporting Enterprise services - Optimalization and logistics monitoring)

```html
<!DOCTYPE html>
<html lang="en">
<head>
<meta charset="utf-8">
<title>Nexaro Solutions</title>
<link href="https://fonts.googleapis.com/css2?family=Michroma&family=Arimo:wght@400;700&display=swap" rel="stylesheet">
<style>
:root{
  --orange:#e2600c;
  --orange-soft:#f08a3c;
  --blue:#0a8ed8;
  --ink:#222;
  --text:#777;
  --muted:#999;
  --band:#efefef;
  --line:#d6d6d6;
  --white:#fff;
}
*{box-sizing:border-box;margin:0;padding:0}
html,body{width:1200px;height:3564px;overflow:hidden;background:var(--white)}
body{font-family:"Arimo",Arial,sans-serif;color:var(--text);position:relative}
.display{font-family:"Michroma",sans-serif;letter-spacing:3px}
section,header,footer{position:absolute;left:0;width:1200px}

/* header */
.site-header{top:0;height:124px;background:var(--white)}
.brand{position:absolute;left:78px;top:36px;display:flex;align-items:center;gap:16px}
.brand-mark{width:46px;height:46px;background:var(--orange)}
.brand-name{font-family:"Michroma",sans-serif;font-size:28px;color:var(--ink);line-height:1}
.brand-name small{display:block;font-size:10px;letter-spacing:8px;margin-top:6px}
.main-nav{position:absolute;right:78px;top:54px;display:flex;gap:42px;font-size:16px;color:var(--ink)}
.main-nav .active{color:var(--orange)}

/* hero */
.hero{top:124px;height:553px;background:linear-gradient(90deg,#a8a49c 0%,#c9b9a4 40%,#d9c8b0 65%,#8d8a86 100%)}
.hero-photo{position:absolute;right:120px;top:0;width:380px;height:553px;background:linear-gradient(180deg,#5a4d44,#2b2a2e)}
.hero-copy{position:absolute;left:78px;top:178px;width:760px}
.hero-title{font-family:"Michroma",sans-serif;font-weight:400;font-size:36px;color:var(--orange);white-space:nowrap;line-height:1.3}
.hero-text{margin-top:18px;font-size:25px;line-height:31px;color:var(--white)}
.hero-dots{position:absolute;left:567px;top:516px;display:flex;gap:12px}
.hero-dots i{width:12px;height:12px;border-radius:50%;border:2px solid var(--white)}
.hero-dots i.on{background:var(--orange);border-color:var(--orange)}

/* partners */
.partners{top:677px;height:126px;background:var(--band);display:flex;justify-content:center;align-items:center;gap:70px}
.partner-badge{width:180px;height:46px;background:#c4c4c4;border-radius:6px}

/* welcome */
.welcome{top:803px;height:582px;text-align:center}
.section-title{font-size:32px;font-weight:400;color:var(--blue);line-height:1.4}
.section-title .accent{color:var(--orange)}
.welcome .section-title{margin-top:50px}
.lead{width:900px;margin:20px auto 0;font-size:14px;line-height:24px;color:var(--muted)}
.services{position:absolute;left:78px;top:257px;width:1046px;display:flex}
.service{width:261.5px;text-align:center;padding:0 10px}
.service-icon{width:104px;height:104px;border-radius:50%;background:#e6e6e6;margin:0 auto;display:flex;align-items:center;justify-content:center}
.service-icon.on{background:var(--orange)}
.service h3{margin-top:22px;font-size:15px;line-height:28px;color:var(--ink);font-weight:400}
.service p{margin-top:6px;font-size:13px;line-height:24px;color:var(--muted)}

/* testimonials */
.testimonials{top:1385px;height:302px;background:var(--band);text-align:center}
.testimonials .section-title{margin-top:48px}
.quote-mark{position:absolute;font-family:Georgia,serif;font-size:150px;color:#d2d2d2;line-height:1}
.quote-open{left:134px;top:54px}
.quote-close{right:134px;top:160px}
.testimonial-text{width:740px;margin:16px auto 0;font-size:14px;line-height:26px;color:#555}
.client{margin-top:18px;font-size:14px;color:#555}
.client b{font-family:"Michroma",sans-serif;font-weight:400;letter-spacing:3px;color:var(--orange);font-size:13px}

/* portfolio */
.portfolio{top:1687px;height:753px;text-align:center}
.portfolio .section-title{margin-top:46px}
.portfolio .lead{margin-top:12px;width:780px;font-size:14px;line-height:24px}
.work-grid{position:absolute;left:78px;top:178px;width:1046px;display:grid;grid-template-columns:repeat(3,333px);gap:17px 23px}
.work{height:209px}
.work-1{background:var(--orange-soft);color:var(--white);padding-top:62px}
.work-1 h4{font-family:"Michroma",sans-serif;font-weight:400;font-size:18px;letter-spacing:2px}
.work-1 p{margin:14px auto 0;width:240px;font-size:14px;line-height:24px}
.work-2{background:linear-gradient(135deg,#d6dde4,#5b6470)}
.work-3{background:linear-gradient(135deg,#e4d8cc,#7a6550)}
.work-4{background:linear-gradient(135deg,#6e7278,#c9cfd6)}
.work-5{background:linear-gradient(135deg,#9ea6ae,#3f4a58)}
.work-6{background:linear-gradient(135deg,#c6ccd4,#5d6a78)}
.btn{display:inline-block;font-family:"Michroma",sans-serif;letter-spacing:2px;color:var(--white);font-size:13px;text-align:center}
.btn-show{position:absolute;left:517px;top:632px;width:166px;height:57px;line-height:57px;background:var(--orange)}

/* contact */
.contact{top:2440px;height:530px;background:var(--orange);text-align:center}
.contact .section-title{margin-top:40px;color:var(--white)}
.contact .section-title .accent{color:var(--blue)}
.contact .lead{margin-top:8px;width:760px;color:var(--white);line-height:24px}
.contact-form{position:absolute;left:240px;top:171px;width:718px}
.field{background:var(--white);height:48px;font-size:14px;color:#888;text-align:left;padding:16px 18px;margin-bottom:9px}
.field-row{display:flex;gap:9px}
.field-row .field{flex:1}
.field.message{height:112px}
.btn-submit{width:166px;height:54px;line-height:54px;background:var(--blue);margin-top:4px}

/* subscribe */
.subscribe{top:2970px;height:247px;background:var(--band);text-align:center}
.subscribe p{margin-top:56px;font-size:16px;line-height:26px;color:#333}
.subscribe-form{position:absolute;left:245px;top:130px;display:flex;gap:12px}
.subscribe-input{width:520px;height:55px;background:var(--white);border:1px solid #bbb;font-size:14px;color:#555;text-align:left;padding:19px 18px}
.btn-subscribe{width:176px;height:55px;line-height:55px;background:var(--orange)}

/* footer */
.site-footer{top:3196px;height:368px;background:var(--band)}
.footer-rule{position:absolute;left:78px;top:21px;width:1046px;height:1px;background:var(--line)}
.footer-col{position:absolute;top:60px;width:333px}
.footer-col h5{font-family:"Michroma",sans-serif;font-weight:400;font-size:15px;letter-spacing:3px;color:var(--orange)}
.footer-col ul{list-style:none;margin-top:22px}
.footer-col li{font-size:14px;line-height:31px;color:#666}
.col-links{left:78px}.col-services{left:435px}.col-contact{left:791px}
.footer-col li.contact-item{display:flex;gap:18px;font-size:14px;line-height:20px;color:#666;margin-bottom:14px}
.contact-item svg{flex:none;margin-top:2px}
.copyright{position:absolute;left:78px;top:331px;font-size:14px;color:#666}
.copyright b{font-weight:400;color:var(--orange)}
.social{position:absolute;right:78px;top:332px;display:flex;gap:22px}
.social i{width:14px;height:14px;border-radius:50%;background:#777}
</style>
</head>
<body>

<header class="site-header">
  <div class="brand">
    <span class="brand-mark"></span>
    <span class="brand-name">NEXARO<small>SOLUTIONS</small></span>
  </div>
  <nav class="main-nav">
    <span class="active">HOME</span><span>ABOUT</span><span>PRODUCTS</span><span>SERVICES</span><span>PORTFOLIO</span><span>CONTACT</span>
  </nav>
</header>

<section class="hero">
  <div class="hero-photo" role="img" aria-label="Photo of a businesswoman in glasses holding a tablet in front of an office building"></div>
  <div class="hero-copy">
    <h1 class="hero-title">NEXARO SOLUTIONS</h1>
    <p class="hero-text">Everything you need to deliver great mobile apps. Deliver native phone, tablet and desktop apps using existing skills, teams, and code.</p>
  </div>
  <div class="hero-dots"><i></i><i class="on"></i><i></i></div>
</section>

<section class="partners" aria-label="Partners">
  <span class="partner-badge"></span><span class="partner-badge"></span><span class="partner-badge"></span><span class="partner-badge"></span>
</section>

<section class="welcome">
  <h2 class="section-title display">WELCOME <span class="accent">TO NEXARO</span></h2>
  <p class="lead">Lorem Ipsum is simply dummy text of the printing and typesetting industry. Lorem Ipsum has been the industry's standard dummy text ever since the 1500s, when an unknown printer took a galley of type and scrambled it to make a type specimen book. t ever since the unknow lley of type and scrambled it to make a type specimen book. It has survived not only five centuries, but also the leap.</p>
  <div class="services">
    <div class="service">
      <div class="service-icon on">
        <svg width="50" height="44" viewBox="0 0 50 44" fill="none" stroke="#fff" stroke-width="2.5"><rect x="3" y="3" width="44" height="28" rx="2"/><path d="M18 41h14M25 31v10M19 13l-5 4 5 4M31 13l5 4-5 4M27 11l-4 12"/></svg>
      </div>
      <h3 class="display">SOFTWARE<br>DEVELOPMENT</h3>
      <p>Lorem Ipsum is simply dummy text of the printing and typesetting simple industry. Lorem</p>
    </div>
    <div class="service">
      <div class="service-icon">
        <svg width="50" height="44" viewBox="0 0 50 44" fill="none" stroke="#444" stroke-width="2.5"><rect x="3" y="3" width="40" height="32" rx="2"/><path d="M3 11h40"/><circle cx="37" cy="33" r="6" fill="#e6e6e6"/><circle cx="37" cy="33" r="2"/></svg>
      </div>
      <h3 class="display">WEB<br>DEVELOPMENT</h3>
      <p>Lorem Ipsum is simply dummy text of the printing and typesetting simple industry. Lorem</p>
    </div>
    <div class="service">
      <div class="service-icon">
        <svg width="44" height="48" viewBox="0 0 44 48" fill="none" stroke="#444" stroke-width="2.5"><path d="M8 3h22l8 8v34H8z"/><path d="M14 16h16M14 23h16M14 30h8M24 36l4 4 8-10"/></svg>
      </div>
      <h3 class="display">ENTERPRISE<br>LEVEL PORTAL</h3>
      <p>Lorem Ipsum is simply dummy text of the printing and typesetting simple industry. Lorem</p>
    </div>
    <div class="service">
      <div class="service-icon">
        <svg width="48" height="48" viewBox="0 0 48 48" fill="none" stroke="#444" stroke-width="2.5"><path d="M4 12l12-5 16 5 12-5v30l-12 5-16-5-12 5z"/><path d="M16 7v30M32 12v30"/><path d="M32 26c-5-6-6-8-6-10a6 6 0 0112 0c0 2-1 4-6 10z" fill="#e6e6e6"/></svg>
      </div>
      <h3 class="display">ROUTE<br>PLANNING</h3>
      <p>Lorem Ipsum is simply dummy text of the printing and typesetting simple industry. Lorem</p>
    </div>
  </div>
</section>

<section class="testimonials">
  <span class="quote-mark quote-open">&ldquo;</span>
  <span class="quote-mark quote-close">&rdquo;</span>
  <h2 class="section-title display">TESTIMONIALS</h2>
  <p class="testimonial-text">" Lorem Ipsum is simply dummy text of the printing and typesetting industry. Lorem Ipsum has been the industry's standard dummy text ever since the 1500s, when an unknown printer took a galley of type and scrambled it to make a type specimen book. It has survived "</p>
  <p class="client"><b>CLIENT NAME</b> - Company CEO</p>
</section>

<section class="portfolio">
  <h2 class="section-title display">OUR <span class="accent">PORTFOLIO</span></h2>
  <p class="lead">" Lorem Ipsum is simply dummy text of the printing and typesetting industry. Lorem Ipsum has been the industry's standard dummy text ever since the 1500s, when an unknown.</p>
  <div class="work-grid">
    <div class="work work-1"><h4>LOREM IPSUM TEXT</h4><p>Lorem Ipsum is simply Tello dummy text of the printing and typesetting.</p></div>
    <div class="work work-2" role="img" aria-label="Photo of two business people talking at an office table"></div>
    <div class="work work-3" role="img" aria-label="Photo of a woman reading a tablet in a cafe"></div>
    <div class="work work-4" role="img" aria-label="Photo of a woman writing at a desk with a laptop"></div>
    <div class="work work-5" role="img" aria-label="Photo of a woman reviewing papers at a desk"></div>
    <div class="work work-6" role="img" aria-label="Photo of a man working on a laptop"></div>
  </div>
  <span class="btn btn-show">SHOW ALL</span>
</section>

<section class="contact">
  <h2 class="section-title display"><span class="accent">CONTACT</span> US</h2>
  <p class="lead">" Lorem Ipsum is simply dummy text of the printing and typesetting industry. Lorem Ipsum has been the industry's standard dummy text ever since the</p>
  <div class="contact-form">
    <div class="field-row"><div class="field">Enter Name</div><div class="field">Enter Contact No.</div></div>
    <div class="field">Enter Email</div>
    <div class="field message">Enter Message</div>
    <span class="btn btn-submit">SUBMIT</span>
  </div>
</section>

<section class="subscribe">
  <p>Fill out our request for a quote form. We will send you an estimated cost<br>for the project as soon as possible.</p>
  <div class="subscribe-form">
    <div class="subscribe-input">EMAIL ID</div>
    <span class="btn btn-subscribe">SUBSCRIBE</span>
  </div>
</section>

<footer class="site-footer">
  <div class="footer-rule"></div>
  <div class="footer-col col-links">
    <h5>QUICK LINKS</h5>
    <ul><li>Home</li><li>About</li><li>Products</li><li>Services</li><li>Portfolio</li><li>Contact</li></ul>
  </div>
  <div class="footer-col col-services">
    <h5>GET SERVICES</h5>
    <ul><li>Software Development</li><li>Web Development</li><li>Enterprise Level Portal</li><li>Route Planning</li></ul>
  </div>
  <div class="footer-col col-contact">
    <h5>GET IN TOUCH</h5>
    <ul>
      <li class="contact-item"><svg width="16" height="20" viewBox="0 0 16 20"><path d="M8 1a7 7 0 00-7 7c0 5 7 11 7 11s7-6 7-11a7 7 0 00-7-7z" fill="var(--orange)"/><circle cx="8" cy="8" r="2.5" fill="#efefef"/></svg><span>NEXARO SOLUTIONS<br>Lorem Ipsum is simple dummy<br>text of print and type setting.</span></li>
      <li class="contact-item"><svg width="18" height="18" viewBox="0 0 18 18" fill="none" stroke="var(--orange)" stroke-width="1.8"><path d="M4 1l3 4-2 2c1 3 3 5 6 6l2-2 4 3-2 3C8 17 1 10 1 3z"/></svg><span>91-555-014-2236</span></li>
      <li class="contact-item"><svg width="18" height="18" viewBox="0 0 18 18" fill="none" stroke="var(--orange)" stroke-width="1.8"><path d="M1 8l16-7-7 16-2-7z"/></svg><span>info@nexarosoft.com</span></li>
    </ul>
  </div>
  <p class="copyright">&copy; <b>NEXARO SOLUTIONS</b> - 2016. All Rights Reserved.</p>
  <div class="social" aria-label="Social links"><i></i><i></i><i></i><i></i></div>
</footer>

</body>
</html>
```